Why my mum deserves a prize! - Mothers Day Competition

Ashgrove Retail Square a local shopping precinct who is running a competition for young children (under 14yrs) to enter. The competition involves writing 'Why my mum deserves a prize!' and sending their entry in (Attention: Events Team - Shop 5/83 Harlow Lane Ashgrove Retail Square Mount Corrindale 3172) We encourage no more than 200 words.
Competition starts: 30th March 2015. Entries close: 6th May 2015. Winners announced by email. See online for Terms and conditions of entry. Entry forms can be downloaded online by visiting www.ashgrovesquare.com.au then please promote in the poster our facebook page and our website. Include that this Competition is proudly organised by the Ashgrove Chamber of Commerce. Please submit the best designs you have as soon as possible as we must have this completed and off to the printers by end of business Friday 27th March 2015. We are open to any designs following the above details and information. thank you. We will require the project in illustrator/adobe ready formats for other editing along the completion.

```html
<!DOCTYPE html>
<html lang="en">
<head>
<meta charset="utf-8">
<title>Why my mum deserves a prize! – Ashgrove Retail Square</title>
<link rel="stylesheet" href="https://fonts.googleapis.com/css2?family=Fredoka:wght@500;600&family=Kalam:wght@400;700&family=Patrick+Hand&family=Indie+Flower&family=Amatic+SC:wght@700&family=PT+Serif&family=Roboto+Slab:wght@800&display=swap">
<style>
  :root {
    --backdrop: #cfcfcf;
    --paper: #f7f7f5;
    --rule-blue: #a9cde8;
    --margin-red: #e58a8a;
    --brand-green: #4e6b22;
    --ink-purple: #5b2a7c;
    --title-pink: #ec2a6f;
    --panel-red: #ee1d4a;
    --text-dark: #1f1f1f;
    --date-red: #e8183f;
    --sun-yellow: #fde21a;
    --sun-orange: #f6c25a;
  }
  * { margin: 0; padding: 0; box-sizing: border-box; }
  html, body { width: 1200px; height: 1000px; overflow: hidden; }
  body { background: var(--backdrop); position: relative; }

  .poster {
    position: absolute; left: 315px; top: 100px;
    width: 585px; height: 825px;
    background-color: var(--paper);
    background-image:
      linear-gradient(to right, transparent 64px, var(--margin-red) 64px, var(--margin-red) 66px, transparent 66px),
      repeating-linear-gradient(to bottom, transparent 0 18px, var(--rule-blue) 18px 19.5px);
    background-position: 0 0, 0 12px;
    overflow: hidden;
    text-align: center;
  }

  .sun-art {
    position: absolute; right: -60px; top: -70px;
    width: 230px; height: 195px; border-radius: 50%;
    background: radial-gradient(circle at 45% 55%, var(--sun-yellow) 0 55%, var(--sun-orange) 80%, #fbe9b0 100%);
  }

  .brand {
    position: absolute; left: 0; right: 0; top: 52px;
    display: flex; justify-content: center; align-items: center; gap: 8px;
    font-family: "Fredoka", sans-serif; font-weight: 600; font-size: 24px;
    color: var(--brand-green);
  }
  .brand-dot { width: 14px; height: 14px; border-radius: 50%; background: var(--brand-green); }

  .presents {
    position: absolute; left: 0; right: 0; top: 100px;
    font-family: "Patrick Hand", cursive; font-size: 15px; color: var(--text-dark);
  }

  .pen-art {
    position: absolute; left: 117px; top: 118px; width: 20px; height: 100px;
    background: linear-gradient(to bottom, #e6e6f2 0 20%, #3f5aa8 20% 100%);
    border-radius: 6px 6px 10px 10px;
  }

  .competition-title {
    position: absolute; left: 142px; top: 118px; width: 325px;
    font-family: "Kalam", cursive; font-weight: 400; font-size: 30px;
    color: var(--ink-purple); text-align: left; letter-spacing: 0.5px;
    border-bottom: 2px solid var(--ink-purple); padding-left: 4px; line-height: 38px;
  }

  .prize-headline {
    position: absolute; left: 0; top: 170px; width: 585px;
    font-family: "Fredoka", sans-serif; font-weight: 500; font-size: 44px;
    line-height: 48px; color: var(--title-pink); text-align: left;
  }
  .prize-headline .line { display: block; white-space: nowrap; }
  .prize-headline .line-one { padding-left: 147px; }
  .prize-headline .line-two { padding-left: 117px; }

  .mum-art {
    position: absolute; left: 205px; top: 268px; width: 150px; height: 240px;
    background: linear-gradient(to bottom, #f4f1ea 0 35%, #8f4fb0 35% 80%, #f4f1ea 80%);
    border-radius: 40% 40% 20% 20%;
  }

  .invite {
    position: absolute; left: 85px; right: 50px; top: 514px;
    font-family: "Indie Flower", cursive; font-size: 28px; line-height: 34px;
    color: var(--ink-purple); white-space: nowrap;
  }

  .entry-panel {
    position: absolute; left: 80px; top: 561px; width: 428px; height: 99px;
    background: var(--panel-red); color: #fff;
  }
  .entry-heading {
    display: inline-block; margin-top: 6px;
    font-family: "Amatic SC", cursive; font-weight: 700; font-size: 22px;
    letter-spacing: 1px; border-bottom: 1.5px solid #fff; line-height: 22px;
  }
  .entry-address {
    margin-top: 10px; font-family: "PT Serif", serif; font-size: 16.5px; line-height: 23px;
  }

  .download-note {
    position: absolute; left: 0; right: 0; top: 676px;
    font-family: "Patrick Hand", cursive; font-size: 24px; line-height: 28px;
    color: var(--text-dark); letter-spacing: 1.4px; white-space: nowrap;
  }
  .website {
    position: absolute; left: 0; right: 0; top: 702px;
    font-family: "Patrick Hand", cursive; font-size: 27px; line-height: 30px; font-weight: 700;
    color: var(--brand-green); letter-spacing: 1.5px;
  }

  .dates {
    position: absolute; left: 0; right: 0; top: 742px;
    font-family: "Roboto Slab", serif; font-weight: 800; font-size: 16px; line-height: 19px;
    color: var(--text-dark);
  }
  .dates .date { color: var(--date-red); }

  .social {
    position: absolute; right: 8px; top: 801px;
    display: flex; align-items: center; gap: 5px;
    font-family: "Roboto Slab", serif; font-weight: 800; font-size: 15px; color: var(--brand-green);
  }
  .social-dot { width: 18px; height: 18px; border-radius: 50%; background: #333; }
</style>
</head>
<body>
  <main class="poster">
    <div class="sun-art" role="img" aria-label="Smiling cartoon sun in the corner"></div>

    <div class="brand"><span class="brand-dot"></span>Ashgrove Retail Square</div>
    <p class="presents">Proudly Presents</p>

    <div class="pen-art" role="img" aria-label="Sketched fountain pen"></div>
    <h2 class="competition-title">Writing Competition</h2>

    <h1 class="prize-headline"><span class="line line-one">"why my mum</span><span class="line line-two">deserves a prize!"</span></h1>

    <div class="mum-art" role="img" aria-label="Child's drawing of a crowned mum holding a gift, with hearts and stars"></div>

    <p class="invite">we invite all little people under 14yrs</p>

    <section class="entry-panel">
      <h3 class="entry-heading">Send your entry to</h3>
      <p class="entry-address">Shop 5/83 Harlow Lane Ashgrove Retail Square,<br>Mount Corrindale 3172.</p>
    </section>

    <p class="download-note">Entry Form can be downloaded online by visting</p>
    <p class="website">www.ashgrovesquare.com.au</p>

    <p class="dates">Competition starts: <span class="date">30th March 2015</span><br>Entries close: <span class="date">6th May 2015</span></p>

    <div class="social"><span class="social-dot"></span>#Ashgroveretailsquare</div>
  </main>
</body>
</html>
```